National Mission Critical Construction Contractor needs Stationery Design to make a bold statement

We are a small commercial construction company, working primarily in mission critical facilities across the U.S.. We have exciting corporate changes going an and a new logo and office space so we need new stationery. The final design should incorporate our new logo and invoke a fresh, high-tech feel while looking simple and modern.

Industry/Entity Type

Construction

Contact Information for Business Card

We are required to list our state licensing qualifications on the back of our card.

Font styles to use
Sans Serif

Requirements
Must have
• We need to have a design for second page of stationery, envelopes both standard and with a window and for a 3 x 4 notepad.

```html
<!DOCTYPE html>
<html lang="en">
<head>
<meta charset="utf-8">
<title>Clearline Construction Management – Stationery</title>
<link href="https://fonts.googleapis.com/css2?family=Michroma&family=Arimo:wght@400;700&display=swap" rel="stylesheet">
<style>
:root{
  --bg:#eceeef;
  --paper:#ffffff;
  --blue:#3aa9e1;
  --brand:#2f7fc1;
  --charcoal:#3b3d40;
  --ink:#4a4a4a;
  --ink-soft:#777;
}
*{margin:0;padding:0;box-sizing:border-box}
html,body{width:1200px;height:937px;overflow:hidden;background:var(--bg)}
body{position:relative;font-family:"Arimo",Arial,sans-serif;color:var(--ink)}
.sheet{position:absolute;background:var(--paper);overflow:hidden}
.sheet svg.swoosh{position:absolute;inset:0;width:100%;height:100%}
.brand{position:absolute;display:flex;align-items:center;gap:6px;color:var(--brand);font-family:"Michroma",sans-serif;font-weight:400}
.brand-mark{border:2px solid var(--brand);border-radius:50%;flex:none}
.brand-name{line-height:1.1;white-space:nowrap}
.brand-name .line2{display:block;letter-spacing:.12em}
.url{position:absolute;font-family:"Michroma",sans-serif;color:#fff;letter-spacing:.14em;white-space:nowrap}

/* letterhead */
.letterhead{left:185px;top:68px;width:385px;height:544px}
.letterhead .brand{left:16px;top:24px}
.letterhead .brand-mark{width:40px;height:40px}
.letterhead .brand-name{font-size:15px}
.letterhead .brand-name .line2{font-size:6px;margin-top:2px}
.contact{position:absolute;font-size:4.6px;line-height:1.6;color:var(--ink)}
.letterhead .contact{left:300px;top:22px}
.contact .ic{display:inline-block;width:4px;height:4px;background:var(--ink-soft);border-radius:50%;margin-right:2px;vertical-align:middle}
.letter{position:absolute;left:36px;top:138px;width:300px;font-size:5.4px;line-height:1.55}
.letter p{margin-bottom:6px}
.letter .gap{margin-bottom:22px}
.letter strong{font-weight:700}
.signature{display:block;width:40px;height:18px;margin:4px 0}

/* folder / second page */
.folder{left:637px;top:40px;width:457px;height:576px}
.folder .brand{left:40px;top:250px}
.folder .brand-mark{width:80px;height:80px;border-width:3px}
.folder .brand-name{font-size:28px}
.folder .brand-name .line2{font-size:10px;margin-top:6px;border-top:1px solid var(--brand);padding-top:4px}
.folder .url{right:22px;bottom:18px;font-size:11px}

/* business cards */
.card{width:176px;height:101px;border-radius:6px}
.card-front{left:46px;top:659px}
.card-front .brand{left:8px;top:9px;gap:4px}
.card-front .brand-mark{width:18px;height:18px;border-width:1.5px}
.card-front .brand-name{font-size:7px}
.card-front .brand-name .line2{font-size:3.2px}
.card-front .contact{left:8px;top:54px;font-size:4px}
.card-person{position:absolute;left:100px;top:56px;font-size:4.2px;line-height:1.4}
.card-person strong{font-weight:700;letter-spacing:.05em}
.card-back{left:46px;top:785px}
.card-back .brand{left:40px;top:40px;gap:4px}
.card-back .brand-mark{width:20px;height:20px;border-width:1.5px}
.card-back .brand-name{font-size:8px}
.card-back .brand-name .line2{font-size:3.6px}

/* envelopes */
.envelope-front{left:265px;top:672px;width:432px;height:208px}
.envelope-front .brand{left:14px;top:20px;gap:5px}
.envelope-front .brand-mark{width:36px;height:36px}
.envelope-front .brand-name{font-size:14px}
.envelope-front .brand-name .line2{font-size:5.5px}
.envelope-back{left:737px;top:672px;width:432px;height:208px}
.envelope-flap{position:absolute;left:0;top:0;width:100%;height:72px;background:var(--blue);border-radius:0 0 34px 34px}
.envelope-back .url{left:0;right:0;top:28px;text-align:center;font-size:11px}
</style>
</head>
<body>

<section class="sheet letterhead" aria-label="Letterhead">
  <svg class="swoosh" viewBox="0 0 385 544" preserveAspectRatio="none" aria-hidden="true">
    <path d="M225,544 C300,520 360,470 385,400 V544 Z" fill="var(--blue)"/>
    <path d="M365,544 C378,520 385,490 385,460 V544 Z" fill="var(--charcoal)"/>
  </svg>
  <div class="brand">
    <span class="brand-mark"></span>
    <span class="brand-name">CLEARLINE<span class="line2">CONSTRUCTION MANAGEMENT</span></span>
  </div>
  <div class="contact">
    200 Harbor Point, Floor 18<br>
    Westfield Road, Suite 4<br>
    <span class="ic"></span>012 345 6789<br>
    <span class="ic"></span>info@clearlinecm.com<br>
    <span class="ic"></span>www.clearlinecm.com
  </div>
  <div class="letter">
    <p>July 2, 2012</p>
    <p><strong>Dear Oli,</strong><br>Harbor Point, Westfield Road</p>
    <p>is simply dummy text of the printing and typesetting industry. Lorem Ipsum has been the industry's standard dummy text ever since the 1500s, when an unknown printer took a galley of type and scrambled it to make a type specimen book. It has survived not only five centuries, but also the leap into electronic typesetting, remaining essentially unchanged. It was popularised in the 1960s with the release of Letraset sheets containing Lorem Ipsum passages, and more recently with desktop publishing software like Aldus PageMaker including versions of Lorem Ipsum.</p>
    <p class="gap">is simply dummy text of the printing and typesetting industry. Lorem Ipsum has been the industry's standard dummy text ever since the 1500s, when an unknown printer took a galley of type and scrambled it to make</p>
    <p>is simply dummy text of the printing and typesetting industry. Lorem Ipsum has been the industry's standard dummy text ever since the 1500s, when an unknown printer took a galley of type and scrambled it to make a type specimen book. It has survived not only five centuries, but also the leap into electronic typesetting, remaining essentially unchanged. It was popularised in the 1960s with the release of Letraset sheets containing Lorem Ipsum passages, and more recently with desktop publishing software like Aldus PageMaker including versions of Lorem Ipsum.</p>
    <p>Best Regards,</p>
    <svg class="signature" viewBox="0 0 40 18" aria-hidden="true"><path d="M2,14 C6,2 8,2 9,14 C12,8 16,8 18,12 C22,6 26,14 32,10" fill="none" stroke="#333" stroke-width="0.8"/></svg>
    <p><strong>Daniel Reyes</strong><br>Director<br><br>Harbor Point, Westfield Road</p>
  </div>
</section>

<section class="sheet folder" aria-label="Second page cover">
  <svg class="swoosh" viewBox="0 0 457 576" preserveAspectRatio="none" aria-hidden="true">
    <path d="M125,576 C330,520 470,280 385,0 H457 V576 Z" fill="var(--blue)"/>
    <path d="M385,0 H457 V240 C445,150 420,70 385,0 Z" fill="var(--charcoal)"/>
  </svg>
  <div class="brand">
    <span class="brand-mark"></span>
    <span class="brand-name">CLEARLINE<span class="line2">CONSTRUCTION MANAGEMENT</span></span>
  </div>
  <div class="url">www.clearlinecm.com</div>
</section>

<section class="sheet card card-front" aria-label="Business card front">
  <svg class="swoosh" viewBox="0 0 176 101" preserveAspectRatio="none" aria-hidden="true">
    <path d="M140,101 C168,80 178,40 150,0 H176 V101 Z" fill="var(--blue)"/>
  </svg>
  <div class="brand">
    <span class="brand-mark"></span>
    <span class="brand-name">CLEARLINE<span class="line2">CONSTRUCTION MANAGEMENT</span></span>
  </div>
  <div class="contact">
    200 Harbor Point, Floor 18<br>
    Westfield Road, Suite 4<br>
    012 345 6789<br>
    info@clearlinecm.com<br>
    www.clearlinecm.com
  </div>
  <div class="card-person"><strong>MARTIN HALE</strong><br>Managing Director</div>
</section>

<section class="sheet card card-back" aria-label="Business card back">
  <div class="brand">
    <span class="brand-mark"></span>
    <span class="brand-name">CLEARLINE<span class="line2">CONSTRUCTION MANAGEMENT</span></span>
  </div>
</section>

<section class="sheet envelope-front" aria-label="Envelope front">
  <svg class="swoosh" viewBox="0 0 432 208" preserveAspectRatio="none" aria-hidden="true">
    <path d="M265,208 C350,170 390,90 355,0 H432 V208 Z" fill="var(--blue)"/>
    <path d="M355,0 H432 V70 C410,40 385,15 355,0 Z" fill="var(--charcoal)"/>
  </svg>
  <div class="brand">
    <span class="brand-mark"></span>
    <span class="brand-name">CLEARLINE<span class="line2">CONSTRUCTION MANAGEMENT</span></span>
  </div>
</section>

<section class="sheet envelope-back" aria-label="Envelope back">
  <div class="envelope-flap"></div>
  <div class="url">www.clearlinecm.com</div>
</section>

</body>
</html>
```